Whitmore Properties
business cards, stationery
Can you please extend the contest ....
can you please extend the contest?
@vElpo - we like the black and gold card in #16 but do not like the gold and white stationary. We would like more black in the stationary with gold being the accent with more focus at the top of the stationary.
The font used in our logo is "Trajanpro" both regular and bold.
kindly tell the font name which is used in your logo ...

```html
<!DOCTYPE html>
<html lang="en">
<head>
<meta charset="utf-8">
<title>Whitmore Properties — Stationery</title>
<link rel="stylesheet" href="https://fonts.googleapis.com/css2?family=Cinzel:wght@400;700&display=swap">
<style>
  :root{
    --page:#ffffff;
    --frame:#d9d9d9;
    --ink:#2a2a2a;
    --charcoal:#262626;
    --charcoal-light:#5b5b5b;
    --accent:#e8731a;
    --accent-soft:#f5a04d;
    --paper:#ffffff;
    --shadow:rgba(0,0,0,.28);
  }
  *{margin:0;padding:0;box-sizing:border-box}
  html,body{width:1200px;height:810px;overflow:hidden;background:var(--page)}
  body{position:relative;font-family:"Cinzel",serif;color:var(--ink)}
  .board{position:absolute;left:19px;top:19px;width:1162px;height:773px;border:1px solid var(--frame)}
  .sheet{position:absolute;background:var(--paper);box-shadow:3px 4px 7px var(--shadow);overflow:hidden}
  .sheet svg.band{position:absolute;left:0;top:0;width:100%;display:block}
  .wordmark{position:absolute;display:flex;align-items:center;gap:7px;font-weight:700;color:var(--ink);letter-spacing:.04em;white-space:nowrap}
  .wordmark .mark{display:block;background:var(--accent)}
  .small-caps{font-variant:small-caps;letter-spacing:.05em;white-space:nowrap}

  .envelope-front{left:65px;top:211px;width:499px;height:202px}
  .envelope-front .band{height:70px}
  .envelope-front .wordmark{left:18px;top:86px;font-size:22px}
  .envelope-front .wordmark .mark{width:22px;height:22px}
  .envelope-front .return-address{position:absolute;left:20px;top:118px;font-size:9.5px;line-height:12px}

  .envelope-back{left:65px;top:446px;width:499px;height:202px}
  .envelope-back svg.flap{position:absolute;inset:0;width:100%;height:100%}
  .envelope-back .wordmark{left:50%;top:86px;transform:translateX(-50%);font-size:11px;gap:5px}
  .envelope-back .wordmark .mark{width:14px;height:14px}

  .letterhead{left:631px;top:125px;width:408px;height:583px}
  .letterhead .band{height:96px}
  .letterhead .wordmark{left:50%;top:96px;transform:translateX(-50%);font-size:21px}
  .letterhead .wordmark .mark{width:22px;height:22px}
  .letterhead .license{position:absolute;left:0;right:0;top:126px;text-align:center;font-size:8.5px}
  .letterhead .footer{position:absolute;left:0;right:0;bottom:34px;text-align:center;font-size:8px;line-height:12px}

  .business-card{left:965px;top:384px;width:187px;height:108px}
  .business-card .wordmark{left:12px;top:14px;font-size:11px;gap:5px}
  .business-card .wordmark .mark{width:12px;height:12px}
  .business-card .person{position:absolute;right:12px;top:38px;text-align:right}
  .business-card .person .name{font-size:7px;font-weight:700}
  .business-card .person .title{font-size:5px}
  .business-card .details{position:absolute;left:12px;bottom:12px;font-size:4.6px;line-height:7px}
</style>
</head>
<body>
<main class="board">

  <section class="sheet envelope-front" aria-label="Envelope front" style="left:46px;top:192px">
    <svg class="band" viewBox="0 0 499 70" preserveAspectRatio="none" aria-hidden="true">
      <defs>
        <linearGradient id="envDark" x1="0" y1="0" x2="0" y2="1">
          <stop offset="0" stop-color="var(--charcoal)"/>
          <stop offset="1" stop-color="var(--charcoal-light)"/>
        </linearGradient>
      </defs>
      <path d="M0 0H499V28Q250 34 0 62Z" fill="url(#envDark)"/>
      <path d="M0 62Q250 34 499 28" fill="none" stroke="var(--accent)" stroke-width="7"/>
      <path d="M0 68Q250 40 499 34" fill="none" stroke="var(--accent-soft)" stroke-width="2"/>
    </svg>
    <div class="wordmark"><span class="mark"></span>Whitmore Properties</div>
    <address class="return-address small-caps" style="font-style:normal">418 Harbor Crest Lane<br>Fairview, Oregon 97024</address>
  </section>

  <section class="sheet envelope-back" aria-label="Envelope back" style="left:46px;top:427px">
    <svg class="flap" viewBox="0 0 499 202" preserveAspectRatio="none" aria-hidden="true">
      <path d="M6 4Q10 20 40 30L230 78Q250 83 270 78L459 30Q489 20 493 4" fill="none" stroke="#9a9a9a" stroke-width="1"/>
    </svg>
    <div class="wordmark"><span class="mark"></span>Whitmore</div>
  </section>

  <section class="sheet letterhead" aria-label="Letterhead" style="left:612px;top:106px">
    <svg class="band" viewBox="0 0 408 96" preserveAspectRatio="none" aria-hidden="true">
      <defs>
        <linearGradient id="lhDark" x1="0" y1="0" x2="0" y2="1">
          <stop offset="0" stop-color="var(--charcoal)"/>
          <stop offset="1" stop-color="var(--charcoal-light)"/>
        </linearGradient>
      </defs>
      <path d="M0 0H408V74Q204 8 0 74Z" fill="url(#lhDark)"/>
      <path d="M0 74Q204 8 408 74" fill="none" stroke="var(--accent)" stroke-width="7"/>
      <path d="M0 82Q204 16 408 82" fill="none" stroke="var(--accent-soft)" stroke-width="2"/>
    </svg>
    <div class="wordmark"><span class="mark"></span>Whitmore Properties</div>
    <p class="license small-caps">License No. 00482915</p>
    <footer class="footer small-caps">
      418 Harbor Crest Lane, Fairview, Oregon 97024<br>
      Phone (503) 555-0142 | Fax (503) 555-0187 | info@whitmoreproperties.net
    </footer>
  </section>

  <section class="sheet business-card" aria-label="Business card" style="left:946px;top:365px">
    <div class="wordmark"><span class="mark"></span>Whitmore</div>
    <div class="person small-caps">
      <p class="name">Dana Marsh</p>
      <p class="title">Project Director</p>
    </div>
    <div class="details small-caps">
      <p>418 Harbor Crest Lane, Fairview, Oregon 97024</p>
      <p>Phone 503.555.0142 · Mobile 503.555.0199</p>
      <p>dmarsh@whitmoreproperties.net</p>
    </div>
  </section>

</main>
</body>
</html>
```